Moden - Mexicali - Flower Shop

brisapetals is looking for a cool web design that has a airy, clean, mexicali feel to it.

See attached images and links for idea of what we mean with the above.

please no templates.

Target Market(s)

Local flower shop in San Diego, California

Industry/Entity Type

Shop

Requirements
Must have
• see. brisapetals.quartzcart.example - I did the site and logo...I love the logo - hate the site.

Going for this feel: http://www.velmorastudio.example/platebook/archives/tovarinos.php

I also attached another site I liked- I just feel like it may be to busy.

```html
<!DOCTYPE html>
<html lang="en">
<head>
<meta charset="utf-8">
<title>Brisapetals – Flower Shop Home</title>
<link rel="stylesheet" href="https://fonts.googleapis.com/css2?family=Roboto:wght@300;400;700&family=Roboto+Condensed:wght@400;700&family=Architects+Daughter&display=swap">
<style>
:root{
  --ink:#222;
  --header:#2b2b2b;
  --orange:#f26b1d;
  --green:#8cc04f;
  --yellow:#e0bf25;
  --dark-btn:#4a4a4a;
  --grey-band:#d8d8d8;
  --paper:#efefef;
  --price:#e8474f;
  --muted:#777;
  --footer:#f6f6f6;
  --white:#fff;
}
*{box-sizing:border-box;margin:0;padding:0}
html,body{width:1200px;height:1000px;overflow:hidden;background:var(--white)}
body{position:relative;font-family:"Roboto",Arial,sans-serif;color:var(--ink)}
.page{position:absolute;left:438px;top:22px;width:342px;height:940px}
.abs{position:absolute}
.heading{font-family:"Roboto Condensed",Arial,sans-serif;font-weight:700;text-align:center;position:absolute;left:0;width:342px}
.btn{position:absolute;display:flex;align-items:center;justify-content:center;color:var(--white);font-family:"Roboto Condensed",Arial,sans-serif}

/* header */
.site-header{left:0;top:0;width:342px;height:54px;background:var(--header)}
.brand{left:46px;top:4px;width:148px;height:29px;background:var(--white);display:flex;align-items:center;justify-content:center;gap:6px;font-family:"Roboto",Arial,sans-serif;font-weight:400;font-size:13px;letter-spacing:3px;color:#6aa9c9;text-transform:uppercase}
.brand-dot{width:10px;height:10px;border-radius:50%;background:#6aa9c9}
.cart{left:240px;top:5px;font-size:4px;color:#ddd;display:flex;align-items:center;gap:3px}
.account-links{left:211px;top:13px;font-size:3.6px;color:#ddd;word-spacing:1px}
.search{left:211px;top:22px;width:86px;height:9px;background:var(--white);font-size:3.6px;color:#aaa;padding:2px 3px}
.search-btn{left:285px;top:22px;width:12px;height:9px;background:var(--green);display:flex;align-items:center;justify-content:center}
.main-nav{left:46px;top:37px;width:250px;height:17px;background:var(--orange);border-radius:2px 2px 0 0;font-size:4.4px;color:var(--white)}
.main-nav span{position:absolute;top:6px;transform:translateX(-50%);white-space:nowrap}

/* hero */
.hero{left:0;top:54px;width:342px;height:122px;background:linear-gradient(120deg,#c8a9ad 0%,#e0557e 25%,#d2bcc1 50%,#a9bf84 75%,#e7b4c3 100%)}
.hero-copy{color:var(--white);font-family:"Roboto",Arial,sans-serif;font-weight:300;text-align:right}
.hero-title{left:190px;top:78px;width:106px;font-size:25px;line-height:1}
.hero-sub{left:190px;top:101px;width:86px;font-size:11px;line-height:1}
.hero-deal{left:170px;top:110px;font-size:34px;line-height:1;font-weight:300}
.hero-deal small{font-size:15px}
.slider-bar{left:0;top:176px;width:342px;height:13px;background:var(--grey-band);display:flex;justify-content:center;align-items:center;gap:1.5px}
.slider-bar i{width:4px;height:4px;border-radius:50%;background:var(--white)}

/* welcome */
.welcome-title{top:200px;font-size:10.5px}
.welcome-text{left:48px;top:215px;width:248px;font-size:4.1px;line-height:6.7px;text-align:center;color:#444}
.btn-green{background:var(--green);font-size:7px}

/* occasions */
.occasions{left:0;top:284px;width:342px;height:112px;background:linear-gradient(135deg,#4a6b63 0%,#6f8a72 35%,#9a8769 60%,#5e7566 100%)}
.occasion{position:absolute;top:0;width:66px;text-align:center;color:var(--white)}
.occasion-icon{position:absolute;top:12px;left:20px;width:26px;height:26px;border-radius:50%;background:var(--orange);display:flex;align-items:center;justify-content:center}
.occasion h3{position:absolute;top:43px;width:100%;font-weight:400;font-size:7px;white-space:nowrap}
.occasion p{position:absolute;top:56px;width:100%;font-size:3.4px;line-height:5px;color:#eee}
.occasion .btn{top:89px;left:17px;width:32px;height:8px;background:var(--orange);font-size:3.4px;font-family:"Roboto",Arial,sans-serif;font-weight:700}

/* collections */
.collections{left:0;top:396px;width:342px;height:165px;background:var(--paper)}
.collections-title{top:405px;font-size:10px}
.product{position:absolute;top:424px;height:98px;background:var(--white)}
.product-photo{position:absolute;left:2px;top:1px;right:2px;height:49px}
.product-name{position:absolute;left:4px;top:56px;font-size:5.5px;color:#555}
.price{position:absolute;left:4px;top:66px;font-family:"Roboto Condensed",Arial,sans-serif;font-weight:700;font-style:italic;font-size:9px;color:var(--price)}
.price s{font-size:5px;color:#333;margin-left:3px}
.add-cart{position:absolute;left:4px;top:80px;width:35px;height:11px;background:var(--green);color:var(--white);font-size:3.6px;display:flex;align-items:center;justify-content:center}
.btn-dark{background:var(--dark-btn);font-size:7px;border:1px solid #333}

/* testimonials */
.testimonials{left:0;top:561px;width:342px;height:174px;background:linear-gradient(120deg,#8a4f8f 0%,#c766a5 40%,#e2a2c9 70%,#b64f8b 100%)}
.testimonials-title{top:568px;font-weight:400;font-family:"Roboto",Arial,sans-serif;color:var(--white);font-size:13.5px}
.review{position:absolute;top:591px;width:72px;height:107px;background:var(--white);overflow:hidden}
.avatar{position:absolute;left:13px;top:7px;width:46px;height:46px;border-radius:50%;background:#a9d2ee}
.reviewer{position:absolute;top:56px;width:100%;text-align:center;font-family:"Architects Daughter",cursive;font-size:6.5px;text-transform:uppercase}
.quote{position:absolute;left:5px;top:69px;width:62px;border-left:1px solid var(--yellow);padding-left:4px;font-size:3.2px;line-height:4.6px;color:#666}
.quote b{color:#888;font-size:6px;line-height:0}
.corner{position:absolute;right:0;bottom:0}

/* contact */
.contact-title{top:742px;font-size:10px;font-weight:400}
.field{position:absolute;border:1px solid #ccc;font-size:3.6px;color:#666;padding:2px 3px;background:var(--white)}
.btn-yellow{background:var(--yellow);font-size:7px}

/* map & footer */
.map{left:0;top:816px;width:342px;height:64px;background:linear-gradient(100deg,#e9e5dc 0%,#dfe8d3 40%,#ece8df 70%,#d9e4cc 100%)}
.site-footer{left:0;top:880px;width:342px;height:47px;background:var(--footer)}
.footer-col{position:absolute;top:4px;font-size:3.7px;line-height:5.2px;color:#888}
.footer-col h4{font-size:5px;color:var(--orange);font-weight:700;line-height:7px}
.footer-col .dark{color:#333}
.social{display:flex;gap:3px;margin-top:3px}
.social i{width:5px;height:5px;background:#6b8fa6}
.bottom-bar{left:0;top:927px;width:342px;height:13px;background:var(--header);color:#bbb;font-size:3.4px;display:flex;align-items:center;justify-content:center}
</style>
</head>
<body>
<div class="page">

  <header class="abs site-header">
    <div class="abs brand"><span>Brisa</span><span class="brand-dot"></span><span>Petals</span></div>
    <div class="abs cart">
      <svg width="6" height="5" viewBox="0 0 12 10"><path d="M0 1h2l2 6h6l2-5H4" fill="none" stroke="#ddd" stroke-width="1.4"/><circle cx="5" cy="9" r="1" fill="#ddd"/><circle cx="9" cy="9" r="1" fill="#ddd"/></svg>
      <span>My Cart: 0 item(s) - $0.00 &#9662;</span>
    </div>
    <div class="abs account-links">Wishlist(0) &nbsp;Checkout &nbsp;Login &nbsp;Create an Account</div>
    <div class="abs search">Search...</div>
    <div class="abs search-btn"><svg width="6" height="6" viewBox="0 0 10 10"><circle cx="4" cy="4" r="3" fill="none" stroke="#fff" stroke-width="1.4"/><path d="M6 6l3 3" stroke="#fff" stroke-width="1.6"/></svg></div>
    <nav class="abs main-nav">
      <span style="left:57px">Home</span>
      <span style="left:89px">About Us</span>
      <span style="left:120px">Shop</span>
      <span style="left:151px">Curated</span>
      <span style="left:187px">Contact Us</span>
    </nav>
  </header>

  <section class="abs hero" role="img" aria-label="Close-up photo of pink carnations with soft green background"></section>
  <div class="abs hero-copy hero-title">Wedding</div>
  <div class="abs hero-copy hero-sub">bouquets</div>
  <div class="abs hero-copy hero-deal">-15<small>%</small></div>
  <div class="abs slider-bar"><i></i><i></i><i></i><i></i></div>

  <h1 class="heading welcome-title">Welcome to Brisapetals</h1>
  <p class="abs welcome-text">Brisapetals is a small flower studio in the heart of San Diego. We gather farm fresh blooms every morning from local growers and arrange them by hand into bright, airy bouquets with a warm Mexicali spirit. From simple stems for a kitchen table to full wedding arrangements, every order is wrapped with care and delivered across the city on the same day. Stop by the shop to see the season's colours, meet our florists, and pick a few favourites to carry home, or let us build a custom piece for your next celebration.</p>
  <div class="btn btn-green" style="left:129px;top:254px;width:82px;height:13px">Read more about us</div>

  <section class="abs occasions" role="img" aria-label="Photo of a meadow of wildflowers in green and orange tones">
    <div class="occasion" style="left:47px">
      <div class="occasion-icon"><svg width="14" height="12" viewBox="0 0 14 12"><path d="M1 4h12L12 1H2z" fill="#fff"/><rect x="2" y="5" width="10" height="6" fill="#fff"/><rect x="5" y="7" width="4" height="4" fill="#f26b1d"/></svg></div>
      <h3>Valentine's Flowers</h3>
      <p>Fresh red roses and bright stems, hand tied the same morning and delivered to your sweetheart's door.</p>
      <div class="btn">Read More</div>
    </div>
    <div class="occasion" style="left:136px">
      <div class="occasion-icon"><svg width="14" height="12" viewBox="0 0 14 12"><path d="M1 4h12L12 1H2z" fill="#fff"/><rect x="2" y="5" width="10" height="6" fill="#fff"/><rect x="5" y="7" width="4" height="4" fill="#f26b1d"/></svg></div>
      <h3>Birthday Flowers</h3>
      <p>Cheerful mixed bouquets in sunny colours, wrapped with care and sent across San Diego on the day.</p>
      <div class="btn">Read More</div>
    </div>
    <div class="occasion" style="left:226px">
      <div class="occasion-icon"><svg width="14" height="12" viewBox="0 0 14 12"><path d="M1 4h12L12 1H2z" fill="#fff"/><rect x="2" y="5" width="10" height="6" fill="#fff"/><rect x="5" y="7" width="4" height="4" fill="#f26b1d"/></svg></div>
      <h3>Plants Arrivals</h3>
      <p>New succulents and potted greens arrive every week, ready for sunny patios and bright kitchen shelves.</p>
      <div class="btn">Read More</div>
    </div>
  </section>

  <section class="abs collections"></section>
  <h2 class="heading collections-title">Curated Collections</h2>
  <div class="product" style="left:46px;width:72px">
    <div class="product-photo" role="img" aria-label="Photo of pink and white lilies" style="background:linear-gradient(135deg,#e7b9d3,#6f8f55)"></div>
    <div class="product-name">California Lilies</div>
    <div class="price">$50.00<s>$ 75.00</s></div>
    <div class="add-cart">ADD TO CART</div>
  </div>
  <div class="product" style="left:136px;width:70px">
    <div class="product-photo" role="img" aria-label="Photo of pink gerbera bouquet in kraft paper" style="background:linear-gradient(135deg,#e66ca0,#b79a7a)"></div>
    <div class="product-name">Ruby Roses</div>
    <div class="price">$40.00<s>$ 75.00</s></div>
    <div class="add-cart">ADD TO CART</div>
  </div>
  <div class="product" style="left:224px;width:71px">
    <div class="product-photo" role="img" aria-label="Photo of yellow and orange lilies" style="background:linear-gradient(135deg,#f0c43a,#e77a2c 60%,#8a8c88)"></div>
    <div class="product-name">Spring time</div>
    <div class="price">$50.00<s>$ 75.00</s></div>
    <div class="add-cart">ADD TO CART</div>
  </div>
  <div class="btn btn-dark" style="left:129px;top:531px;width:83px;height:14px">More Collections</div>

  <section class="abs testimonials" role="img" aria-label="Photo of pink blossoms with soft purple background"></section>
  <h2 class="heading testimonials-title">Our Testimonials</h2>
  <div class="review" style="left:47px">
    <div class="avatar" role="img" aria-label="Portrait of customer Owen Reyes"></div>
    <div class="reviewer">Owen Reyes</div>
    <p class="quote"><b>&ldquo;</b> Lovely flowers and friendly people, my order came right on time and looked great.</p>
    <svg class="corner" width="22" height="22" viewBox="0 0 22 22"><path d="M22 0V22H0z" fill="#222"/><path d="M15 14v6M12 17h6" stroke="#fff" stroke-width="1"/></svg>
  </div>
  <div class="review" style="left:136px">
    <div class="avatar" role="img" aria-label="Portrait of customer Clara Dunne"></div>
    <div class="reviewer">Clara Dunne</div>
    <p class="quote"><b>&ldquo;</b> Beautiful bouquet for my mother, fresh for over a week and so nicely wrapped.</p>
    <svg class="corner" width="22" height="22" viewBox="0 0 22 22"><path d="M22 0V22H0z" fill="#222"/><path d="M15 14v6M12 17h6" stroke="#fff" stroke-width="1"/></svg>
  </div>
  <div class="review" style="left:224px">
    <div class="avatar" role="img" aria-label="Portrait of customer Farid Osman"></div>
    <div class="reviewer">Farid Osman</div>
    <p class="quote"><b>&ldquo;</b> Great service for our office plants, easy ordering and quick local delivery.</p>
    <svg class="corner" width="22" height="22" viewBox="0 0 22 22"><path d="M22 0V22H0z" fill="#222"/><path d="M15 14v6M12 17h6" stroke="#fff" stroke-width="1"/></svg>
  </div>
  <div class="btn btn-green" style="left:132px;top:709px;width:83px;height:13px">Read more about us</div>

  <h2 class="heading contact-title">Quick Contact</h2>
  <div class="field" style="left:45px;top:759px;width:80px;height:12px">Name</div>
  <div class="field" style="left:131px;top:759px;width:79px;height:12px">Email</div>
  <div class="field" style="left:216px;top:759px;width:79px;height:24px">Message</div>
  <div class="field" style="left:45px;top:773px;width:80px;height:11px">Phone</div>
  <div class="field" style="left:131px;top:773px;width:79px;height:11px">Subject</div>
  <div class="btn btn-yellow" style="left:129px;top:791px;width:83px;height:15px">Send Massage</div>

  <section class="abs map" role="img" aria-label="Street map of the shop's San Diego neighbourhood"></section>

  <footer class="abs site-footer">
    <div class="footer-col" style="left:46px">
      <h4>Quick Link</h4>
      Home<br>About Us<br>Shop<br>Curated<br>Contact Us
    </div>
    <div class="footer-col" style="left:133px;width:70px">
      <h4>Meet Brisa</h4>
      Based in Hillcrest, San Diego - We offer farm fresh, curated, care and same day delivery flower bouquets.
      <div class="social"><i></i><i></i><i></i></div>
    </div>
    <div class="footer-col" style="left:240px">
      <h4>Reach Brisa</h4>
      2210 Palma Avenue<br>San Diego, CA 92199<br>
      <span class="dark">Email: info@brisapetals.example</span><br>
      <span class="dark">Phone: 619-555-0147</span>
    </div>
  </footer>
  <div class="abs bottom-bar">Copyright © 2014 Brisapetals of San Diego. Website builder by QuartzCart.</div>

</div>
</body>
</html>
```